orbit wellness loft
Project: logo for fitness studio
logo for fitness studio - Health
logo for fitness studio
Simple
Laura Whitfield
Certified Personal Trainer
482 W. Timber Ridge Rd. ElReno Ok. 73021
orbitwellness.owl@examplemail.test
I have already sent you most of my information .If you need more let me know .
Donna01 Donna01
I can't figure out how to change my brief. The email is wrong it's .owl@examplemail.test not .wol@examplemail.test so sorry. Also not so sure I like the black. The feeling I'm after is beach, sun and sand etc. thanks

```html
<!DOCTYPE html>
<html lang="en">
<head>
<meta charset="utf-8">
<title>orbit wellness loft – business card</title>
<link href="https://fonts.googleapis.com/css2?family=Open+Sans:wght@300;400;700&display=swap" rel="stylesheet">
<style>
  :root {
    --teal: #1fb5b8;
    --teal-dark: #138f93;
    --ink: #2b2b2b;
    --deep-sea: #0f3a44;
    --grey: #c9c3b4;
    --paper: #ffffff;
    --backdrop: #e9ecec;
  }
  * { box-sizing: border-box; margin: 0; padding: 0; }
  html, body { width: 1200px; height: 782px; overflow: hidden; }
  body {
    background: var(--backdrop);
    font-family: "Open Sans", Arial, sans-serif;
    position: relative;
  }
  .card {
    position: absolute;
    top: 236px;
    width: 540px;
    height: 309px;
    border-radius: 16px;
    overflow: hidden;
    box-shadow: 0 6px 18px rgba(0,0,0,0.18);
  }
  .card-back { left: 40px; background: var(--deep-sea); }
  .card-front { left: 620px; background: var(--paper); }
  .card-art { position: absolute; inset: 0; }

  .brand {
    position: absolute;
    display: flex;
    flex-direction: column;
    align-items: center;
    gap: 8px;
    color: var(--teal);
    font-weight: 300;
    text-align: center;
  }
  .brand-dot {
    width: 46px; height: 46px;
    border-radius: 50%;
    border: 2px solid var(--teal);
  }
  .brand-name { font-size: 28px; line-height: 1.05; letter-spacing: 0.3px; }
  .card-back .brand { left: 0; right: 0; top: 128px; }
  .card-front .brand { left: 30px; width: 210px; top: 148px; }
  .card-front .brand-name { font-size: 26px; }

  .person {
    position: absolute;
    right: 26px;
    top: 80px;
    text-align: right;
  }
  .person-name { font-size: 15px; font-weight: 700; color: var(--teal-dark); }
  .person-role { font-size: 12px; color: var(--teal); margin-top: 1px; }

  .divider {
    position: absolute;
    left: 262px;
    top: 178px;
    width: 1px;
    height: 92px;
    background: var(--grey);
  }
  .contact {
    position: absolute;
    left: 276px;
    top: 176px;
    list-style: none;
    font-size: 11.5px;
    line-height: 15.5px;
    color: var(--ink);
  }
  .contact li { display: flex; align-items: center; gap: 5px; white-space: nowrap; }
  .contact .indent { padding-left: 15px; }
  .contact svg { width: 10px; height: 10px; flex: none; fill: var(--teal-dark); }
</style>
</head>
<body>

<section class="card card-back" aria-label="Card back">
  <svg class="card-art" viewBox="0 0 540 309" aria-hidden="true">
    <path d="M0 0 H540 V40 C420 36 260 60 0 138 Z" fill="var(--teal)"/>
    <path d="M0 138 C260 60 420 36 540 40 V52 C420 50 260 76 0 152 Z" fill="var(--grey)"/>
  </svg>
  <div class="brand">
    <span class="brand-dot"></span>
    <span class="brand-name">orbit wellness<br>loft</span>
  </div>
</section>

<section class="card card-front" aria-label="Card front">
  <svg class="card-art" viewBox="0 0 540 309" aria-hidden="true">
    <path d="M0 0 H540 V0 C420 6 250 20 0 62 Z" fill="var(--teal)"/>
    <path d="M0 62 C250 20 420 6 540 0 V12 C420 18 250 34 0 74 Z" fill="var(--grey)"/>
    <path d="M250 309 C380 300 470 268 540 218 V309 Z" fill="var(--teal)"/>
  </svg>

  <div class="person">
    <p class="person-name">Laura Whitfield</p>
    <p class="person-role">Consultant</p>
  </div>

  <div class="brand">
    <span class="brand-dot"></span>
    <span class="brand-name">orbit wellness<br>loft</span>
  </div>

  <div class="divider"></div>

  <ul class="contact">
    <li><svg viewBox="0 0 10 10"><path d="M5 0a3.5 3.5 0 0 0-3.5 3.5C1.5 6 5 10 5 10s3.5-4 3.5-6.5A3.5 3.5 0 0 0 5 0zm0 5a1.4 1.4 0 1 1 0-2.8A1.4 1.4 0 0 1 5 5z"/></svg>214, 6th floor, Harbor Walk Road</li>
    <li class="indent">ELR</li>
    <li><svg viewBox="0 0 10 10"><path d="M2 0l2 2.4-1.1 1.3a6 6 0 0 0 3.4 3.4L7.6 6 10 8l-1.3 1.8C4.5 10 0 5.5.2 1.3z"/></svg>012 555 0189</li>
    <li><svg viewBox="0 0 10 10"><rect x="2.5" y="0" width="5" height="10" rx="1"/></svg>012 555 0189</li>
    <li><svg viewBox="0 0 10 10"><path d="M0 2h10v6H0z M0 2l5 3.5L10 2" stroke="#fff" stroke-width=".8"/></svg>hello@examplemail.test</li>
    <li class="indent">www.orbitwellness.test</li>
  </ul>
</section>

</body>
</html>
```